Consulting company business cards

We have a base design, but would be willing to update. We have a new logo/"tag" that needs to be added. Current business card design is attached for reference into our "style."

Industry/Entity Type

Business

Contact Information for Business Card

Should contain name and title, office number, mobile number if appropriate, e-mail, website, physical address, and company logo.

Font styles to use
Other font styles liked:
• See current card design on GorvandBCard

Colors
0455a3
85acd3
aaaaaa

Requirements
Must have
• Our colors are navy blue, gray, and a lighter blue
Nice to have
• Design that I can easily drop in new names/titles as we hire employees.

```html
<!DOCTYPE html>
<html lang="en">
<head>
<meta charset="utf-8">
<title>Torvik Business Cards</title>
<link href="https://fonts.googleapis.com/css2?family=Open+Sans:wght@400;600;800&display=swap" rel="stylesheet">
<style>
  :root {
    --navy: #0c3351;
    --light-blue: #85acd3;
    --white: #ffffff;
    --gray: #aaaaaa;
    --backdrop: #ecebe8;
    --text-font: "Open Sans", Arial, sans-serif;
  }
  * { box-sizing: border-box; margin: 0; padding: 0; }
  html, body {
    width: 1200px;
    height: 900px;
    overflow: hidden;
    background: var(--backdrop);
    font-family: var(--text-font);
  }
  .sheet { position: relative; width: 1200px; height: 900px; }
  .card {
    position: absolute;
    left: 250px;
    width: 700px;
    height: 400px;
    overflow: hidden;
    box-shadow: 0 6px 18px rgba(0,0,0,0.18);
  }
  .card--front { top: 35px; background: var(--navy); }
  .card--back { top: 465px; background: var(--white); }

  .brand {
    position: absolute;
    display: flex;
    flex-direction: column;
    align-items: flex-start;
  }
  .brand__row { display: flex; align-items: center; gap: 14px; }
  .brand__name {
    font-family: var(--text-font);
    font-weight: 800;
    font-size: 88px;
    line-height: 0.95;
    letter-spacing: 2px;
  }
  .brand__dot { width: 40px; height: 40px; border-radius: 50%; }
  .brand__tagline {
    margin-top: 6px;
    margin-left: 28px;
    font-size: 16px;
    font-weight: 400;
    letter-spacing: 3px;
  }
  .card--front .brand { left: 150px; top: 130px; }
  .card--front .brand__name,
  .card--front .brand__tagline { color: var(--white); }
  .card--front .brand__dot { background: var(--white); }

  .card--back .brand { left: 180px; top: 36px; }
  .card--back .brand__name,
  .card--back .brand__tagline { color: var(--navy); }
  .card--back .brand__dot { background: var(--light-blue); }

  .details-band {
    position: absolute;
    left: 0;
    top: 180px;
    width: 700px;
    height: 220px;
    background: var(--navy);
    color: var(--white);
  }
  .person { position: absolute; left: 40px; top: 98px; }
  .person__name { font-size: 21px; font-weight: 600; line-height: 1.25; }
  .person__title { font-size: 17px; font-weight: 400; line-height: 1.3; }
  .person__address { font-size: 17px; line-height: 1.3; margin-top: 12px; }

  .contact-list {
    position: absolute;
    right: 30px;
    top: 18px;
    list-style: none;
    text-align: right;
    font-size: 14px;
    line-height: 1.6;
    color: var(--white);
  }
  .contact-list li { display: flex; justify-content: flex-end; align-items: center; gap: 7px; }
  .contact-list svg { width: 11px; height: 11px; fill: var(--white); flex: none; }
</style>
</head>
<body>
<main class="sheet">

  <section class="card card--front" aria-label="Card front">
    <div class="brand">
      <div class="brand__row">
        <span class="brand__name">TORVIK</span>
        <span class="brand__dot"></span>
      </div>
      <span class="brand__tagline">A CLOUD CONSULTING COMPANY</span>
    </div>
  </section>

  <section class="card card--back" aria-label="Card back">
    <div class="brand">
      <div class="brand__row">
        <span class="brand__name">TORVIK</span>
        <span class="brand__dot"></span>
      </div>
      <span class="brand__tagline">A CLOUD CONSULTING COMPANY</span>
    </div>

    <div class="details-band">
      <ul class="contact-list">
        <li>555.014.2910
          <svg viewBox="0 0 12 12" aria-hidden="true"><path d="M2 1h2.5l1 3-1.5 1a7 7 0 0 0 3 3l1-1.5 3 1V11a1 1 0 0 1-1 1A10 10 0 0 1 0 2a1 1 0 0 1 1-1z"/></svg>
        </li>
        <li>555.014.2971
          <svg viewBox="0 0 12 12" aria-hidden="true"><path d="M3 0h5l1 1v3h2v8H1V4h2zM4 1v3h4V1zM3 6v1h6V6zM3 8v1h6V8z"/></svg>
        </li>
        <li>torviktech.com
          <svg viewBox="0 0 12 12" aria-hidden="true"><path d="M0 2h12v8H0zM1 3l5 4 5-4z" fill-rule="evenodd"/></svg>
        </li>
        <li>dgorvand@torviktech.com
          <svg viewBox="0 0 12 12" aria-hidden="true"><path d="M0 2h12v8H0zM1 3l5 4 5-4z" fill-rule="evenodd"/></svg>
        </li>
        <li>www.torviktech.com
          <svg viewBox="0 0 12 12" aria-hidden="true"><path d="M6 0a6 6 0 1 0 0 12A6 6 0 0 0 6 0zm0 1.2a4.8 4.8 0 1 1 0 9.6 4.8 4.8 0 0 1 0-9.6zM1.5 5.5h9v1h-9zM5.5 1.5h1v9h-1z"/></svg>
        </li>
      </ul>

      <div class="person">
        <p class="person__name">Dana Gorvand</p>
        <p class="person__title">Managing Director</p>
        <p class="person__address">1870 W 48 th lakeview<br>ohio 40112</p>
      </div>
    </div>
  </section>

</main>
</body>
</html>
```